Business Card Design Project

We need a Business Card for an Mechanical Engineering firm in Singapore. The design should be Modern & Technical looking, yet eye catching.

Our company deals in Cutting Tools & Machine Accessories for the Manufacturing Industries such as Oil & Gas, Aero Space, etc... For more information on our Company, you can either email me or view our website www.valtrion.com.sg.

We are trying to revamp our image to give our consumers a fresh new perspective to our company, so we welcome all ideas.

Industry/Entity Type

Business

Requirements
Must have
• Must incorporate New Company Logo into the card as shown in Uploaded file.

```html
<!DOCTYPE html>
<html lang="en">
<head>
<meta charset="utf-8">
<title>Valtrion Tools – Business Card</title>
<link href="https://fonts.googleapis.com/css2?family=Comfortaa:wght@600;700&display=swap" rel="stylesheet">
<style>
  :root {
    --backdrop: #3c3c3e;
    --silver-light: #eef0f4;
    --silver-mid: #c9ccd4;
    --silver-dark: #aeb2bc;
    --slate-light: #5a5868;
    --slate-dark: #34323f;
    --wave-white: #ffffff;
    --brand-red: #a51d2f;
    --text-white: #ffffff;
  }
  html, body {
    margin: 0;
    padding: 0;
    width: 1200px;
    height: 900px;
    overflow: hidden;
    background: var(--backdrop);
  }
  .canvas {
    position: relative;
    width: 1200px;
    height: 900px;
    display: flex;
    align-items: center;
    justify-content: center;
  }
  .business-card {
    position: relative;
    width: 900px;
    height: 514px;
    overflow: hidden;
    box-shadow: 0 18px 40px rgba(0, 0, 0, 0.45);
    font-family: "Comfortaa", "Trebuchet MS", sans-serif;
  }
  .card-surface {
    position: absolute;
    inset: 0;
    width: 100%;
    height: 100%;
  }
  .brand-block {
    position: absolute;
    left: 48px;
    top: 52px;
  }
  .brand-name {
    display: flex;
    align-items: center;
    gap: 12px;
    color: var(--brand-red);
    font-weight: 700;
    font-size: 30px;
    letter-spacing: 2px;
    text-transform: uppercase;
    margin: 0;
  }
  .brand-dot {
    width: 22px;
    height: 22px;
    border-radius: 50%;
    background: var(--brand-red);
    flex: none;
  }
  .website {
    margin: 14px 0 0 6px;
    color: var(--text-white);
    font-weight: 700;
    font-size: 32px;
    letter-spacing: 1px;
    text-shadow: 0 1px 2px rgba(0, 0, 0, 0.25);
  }
  .contact-list {
    position: absolute;
    left: 640px;
    top: 285px;
    margin: 0;
    padding: 0;
    list-style: none;
    color: var(--text-white);
    font-weight: 700;
    font-size: 38px;
    line-height: 1.12;
    letter-spacing: 1px;
  }
  .contact-list .email {
    margin-top: 22px;
  }
</style>
</head>
<body>
<main class="canvas">
  <article class="business-card">
    <svg class="card-surface" viewBox="0 0 900 514" preserveAspectRatio="none" aria-hidden="true">
      <defs>
        <linearGradient id="silverFace" x1="0" y1="0" x2="1" y2="1">
          <stop offset="0" stop-color="var(--silver-dark)"/>
          <stop offset="0.45" stop-color="var(--silver-mid)"/>
          <stop offset="0.8" stop-color="var(--silver-light)"/>
          <stop offset="1" stop-color="#ffffff"/>
        </linearGradient>
        <linearGradient id="slateFace" x1="0" y1="0" x2="1" y2="1">
          <stop offset="0" stop-color="var(--slate-dark)"/>
          <stop offset="0.6" stop-color="var(--slate-light)"/>
          <stop offset="1" stop-color="#6a6878"/>
        </linearGradient>
      </defs>
      <rect class="upper-panel" width="900" height="514" fill="url(#silverFace)"/>
      <path class="lower-panel"
            d="M0,302 C120,272 230,250 330,278 C420,304 480,262 580,252 C690,242 760,228 900,150 L900,514 L0,514 Z"
            fill="url(#slateFace)"/>
      <path class="wave-line"
            d="M0,302 C120,272 230,250 330,278 C420,304 480,262 580,252 C690,242 760,228 900,150"
            fill="none" stroke="var(--wave-white)" stroke-width="9"/>
    </svg>

    <header class="brand-block">
      <p class="brand-name"><span>Valtrion Tools</span><span class="brand-dot"></span></p>
      <p class="website">Website</p>
    </header>

    <ul class="contact-list">
      <li class="name">Name</li>
      <li class="mobile">Mobile</li>
      <li class="address">Address</li>
      <li class="email">E-mail</li>
    </ul>
  </article>
</main>
</body>
</html>
```